Brackwell Immigration Law

We need a web design for our existing company www.brackwellcounsel.co.uk. We are an immigration consultancy. The final design should communicate professionalism, integrity and affordability.

Industry/Entity Type

It Company

Logo Text

Brackwell Counsel Partners

Number of Pages Required

5+ page

Font styles to use
Serif

Requirements
Must have
• I want to have the same silhouette logo but something different in positioning..
Nice to have
• Please have a look at these websites:
• https://www.travelpathguide.co.uk/visa_uk/
• http://www.oakdenadvisers.co.uk/
• http://www.myrtlegatelaw.org/index.php
• www.brackwellcounsel.co.uk

```html
<!DOCTYPE html>
<html lang="en">
<head>
<meta charset="utf-8">
<title>Brackwell Counsel Partners — Immigration Law</title>
<link href="https://fonts.googleapis.com/css2?family=Noto+Serif:wght@700&family=Open+Sans:wght@400;600;700&display=swap" rel="stylesheet">
<style>
:root{
  --maroon:#7b1c36;
  --maroon-dark:#5e1228;
  --ink:#333333;
  --muted:#777777;
  --rule:#e3e3e3;
  --paper:#ffffff;
  --soft:#f5f5f5;
  --footer:#2d2d2d;
  --footer-bottom:#1f1f1f;
  --footer-text:#b5b5b5;
}
*{box-sizing:border-box;margin:0;padding:0}
html,body{width:1200px;height:2696px;overflow:hidden}
body{font-family:"Open Sans",Arial,sans-serif;color:var(--ink);background:var(--paper);position:relative;font-size:13px;line-height:1.6}
.wrap{position:absolute;left:100px;width:1000px}
a{color:inherit;text-decoration:none}
.btn{display:inline-block;background:var(--maroon);color:#fff;font-size:12px;font-weight:600;padding:7px 16px;border-radius:2px}
.btn::after{content:" \203A"}

/* header */
.site-header{position:absolute;top:0;left:0;width:1200px;height:120px}
.brand{position:absolute;left:100px;top:28px}
.brand-name{font-family:"Noto Serif",Georgia,serif;font-weight:700;font-size:30px;color:var(--maroon);line-height:1.1}
.brand-sub{font-family:"Noto Serif",Georgia,serif;font-weight:700;font-size:12px;color:var(--maroon);margin-left:150px;margin-top:2px}
.account{position:absolute;right:100px;top:22px;font-size:12px;color:var(--muted)}
.account span{margin-left:14px}
.social-row{position:absolute;right:100px;top:52px;display:flex;gap:6px;align-items:center}
.social-row i{display:block;width:22px;height:22px;border-radius:3px}
.lang{width:64px;height:22px;border:1px solid var(--rule);display:flex;align-items:center;gap:5px;padding:0 5px;font-size:10px;color:var(--muted);margin-left:6px}
.lang b{width:18px;height:12px;background:#c9c9d6;display:block}

/* hero */
.hero{position:absolute;top:120px;left:0;width:1200px;height:620px}
.hero-photo{position:absolute;inset:0;background:linear-gradient(100deg,#6d5b52 0%,#3b3433 35%,#8d7c72 60%,#2c2626 100%)}
.main-nav{position:absolute;top:32px;left:100px;width:1000px;height:50px;background:var(--maroon);display:flex;align-items:center;padding:0 14px}
.main-nav a{color:#fff;font-size:12px;font-weight:600;padding:0 22px;letter-spacing:.3px}
.main-nav a.active{color:#f1c7d3}
.search{margin-left:auto;width:210px;height:28px;background:#fff;border-radius:2px;position:relative;font-size:11px;color:#999;padding:5px 10px}
.search svg{position:absolute;right:8px;top:7px}
.hero-copy{position:absolute;right:100px;top:250px;width:420px;text-align:right;color:#fff}
.hero-copy h1{font-size:26px;font-weight:700;letter-spacing:.5px;background:rgba(0,0,0,.35);display:inline-block;padding:4px 10px}
.hero-copy p{font-size:12px;margin:10px 0 18px;color:#eee}
.dots{position:absolute;right:110px;bottom:30px;display:flex;gap:8px}
.dots i{width:10px;height:10px;border-radius:50%;background:rgba(255,255,255,.5);display:block}
.dots i:first-child{background:#fff}

/* welcome */
.welcome{top:775px;height:230px}
.welcome h2{font-size:22px;font-weight:600;color:var(--maroon);margin-bottom:14px}
.welcome p{width:680px;color:var(--muted);font-size:12px;margin-bottom:20px}
.welcome-photo{position:absolute;right:0;top:70px;width:240px;height:130px;border:6px solid #fff;box-shadow:0 1px 6px rgba(0,0,0,.25);background:linear-gradient(135deg,#d9cfc7,#9c8f9a)}
.section-rule{position:absolute;left:0;width:1200px;height:1px;background:var(--rule)}

/* services */
.section-title{text-align:center;font-size:22px;font-weight:600;color:var(--maroon)}
.section-lede{text-align:center;font-size:13px;color:var(--muted);margin-top:4px}
.services{top:1025px}
.service-grid{display:flex;justify-content:space-between;margin-top:38px;padding:0 20px}
.service{width:210px;text-align:center}
.service-icon{width:100px;height:100px;margin:0 auto;border-radius:50%;background:#fff;box-shadow:0 2px 8px rgba(0,0,0,.2);display:flex;align-items:center;justify-content:center}
.service h3{font-size:12px;font-weight:700;margin:24px 0 8px;letter-spacing:.4px}
.service p{font-size:11px;color:var(--muted);margin-bottom:14px;line-height:1.5}

/* team */
.team{top:1500px}
.team h2{font-size:22px;font-weight:600;color:var(--maroon)}
.pager{position:absolute;right:0;top:6px;display:flex;gap:3px}
.pager i{width:20px;height:20px;background:var(--soft);border:1px solid var(--rule);font-style:normal;font-size:12px;text-align:center;line-height:17px;color:#555}
.team-grid{display:flex;justify-content:space-between;margin-top:26px}
.member{width:232px;text-align:center}
.member-photo{height:180px;border:5px solid #fff;box-shadow:0 1px 6px rgba(0,0,0,.25)}
.member h3{font-size:13px;font-weight:700;margin:18px 0 6px}
.member p{font-size:11px;color:var(--muted);line-height:1.5}
.member-social{display:flex;justify-content:center;gap:6px;margin-top:10px}
.member-social i{width:20px;height:20px;border-radius:50%;display:block}

/* news */
.news{top:1940px;width:1000px}
.news h2{font-size:22px;font-weight:600;color:var(--maroon);margin-bottom:22px}
.news-list{width:660px}
.news-item{display:flex;gap:22px;margin-bottom:26px}
.news-photo{width:120px;height:110px;flex:none;border:4px solid #fff;box-shadow:0 1px 6px rgba(0,0,0,.25);background:linear-gradient(135deg,#d8d3cf,#6f6a6c)}
.news-item time{font-size:11px;color:var(--muted);display:block;margin-bottom:4px}
.news-item p{font-size:11.5px;color:var(--muted);line-height:1.55;margin-bottom:6px}
.news-item .more{font-size:11px;color:var(--maroon);font-weight:600}
.sidebar{position:absolute;right:0;top:0;width:250px}
.sidebar h3{font-size:18px;font-weight:600;color:var(--maroon);padding-bottom:10px;border-bottom:2px solid var(--maroon);margin-bottom:8px}
.sidebar li{list-style:none;font-size:11.5px;color:#555;padding:8px 0 8px 16px;border-bottom:1px solid var(--rule);position:relative}
.sidebar li::before{content:"";position:absolute;left:2px;top:14px;border-left:5px solid var(--maroon);border-top:4px solid transparent;border-bottom:4px solid transparent}

/* footer */
.site-footer{position:absolute;top:2420px;left:0;width:1200px;height:220px;background:var(--footer);color:var(--footer-text)}
.footer-cols{position:absolute;left:100px;top:34px;width:1000px;display:flex;justify-content:space-between}
.footer-cols h4{font-size:11px;font-weight:700;color:#fff;text-transform:uppercase;margin-bottom:14px;letter-spacing:.5px}
.footer-links li{list-style:none;font-size:11px;line-height:2}
.newsletter{width:300px}
.newsletter p{font-size:11px;margin-bottom:10px}
.newsletter .field{width:170px;height:28px;background:#fff;border-radius:2px;font-size:10px;color:#999;padding:6px 8px;margin-bottom:10px}
.newsletter .btn{padding:6px 14px;font-size:11px}
.newsletter .btn::after{content:""}
.contact{width:300px}
.contact li{list-style:none;font-size:11px;line-height:1.9;padding-left:14px;position:relative}
.contact li::before{content:"";position:absolute;left:0;top:7px;width:6px;height:6px;background:var(--maroon);border-radius:50%}
.contact b{color:#fff;font-weight:600}
.footer-bottom{position:absolute;top:2640px;left:0;width:1200px;height:56px;background:var(--footer-bottom);color:var(--footer-text);font-size:11px}
.footer-bottom .copy{position:absolute;left:100px;top:20px}
.footer-bottom .follow{position:absolute;right:100px;top:17px;display:flex;gap:5px;align-items:center}
.footer-bottom .follow i{width:18px;height:18px;display:block;border-radius:2px}
.c1{background:#e4572e}.c2{background:#3b5998}.c3{background:#1da1f2}.c4{background:#c4302b}.c5{background:#0e76a8}.c6{background:#dd4b39}
</style>
</head>
<body>

<header class="site-header">
  <div class="brand">
    <div class="brand-name">Brackwell Counsel Partners</div>
    <div class="brand-sub">Immigration Law</div>
  </div>
  <div class="account"><span>Log In</span><span>|</span><span>Sign Up</span></div>
  <div class="social-row">
    <i class="c1"></i><i class="c2"></i><i class="c3"></i><i class="c4"></i><i class="c5"></i><i class="c6"></i>
    <div class="lang"><b></b>EN ▾</div>
  </div>
</header>

<section class="hero">
  <div class="hero-photo" role="img" aria-label="Photograph of a team of lawyers in business suits standing together in an office"></div>
  <nav class="main-nav">
    <a class="active">HOME</a><a>ABOUT US ▾</a><a>JOIN US</a><a>CONTACT US</a><a>BLOG</a>
    <div class="search">Search
      <svg width="14" height="14" viewBox="0 0 14 14"><circle cx="6" cy="6" r="4.5" fill="none" stroke="#777" stroke-width="1.6"/><line x1="9.5" y1="9.5" x2="13" y2="13" stroke="#777" stroke-width="1.6"/></svg>
    </div>
  </nav>
  <div class="hero-copy">
    <h1>IMMIGRATION CONSULTANCY</h1>
    <p>Clear, honest and affordable advice on every kind of UK visa, settlement and appeal, handled by qualified and caring advisers.</p>
    <a class="btn">READ MORE</a>
  </div>
  <div class="dots"><i></i><i></i><i></i></div>
</section>

<section class="wrap welcome">
  <h2>Welcome to Brackwell Counsel Partners!</h2>
  <p>Brackwell Counsel Partners is regulated by the Immigration Advisory Standards Board and we have built our reputation on good quality legal work, honest advice and fair fees across a wide range of immigration matters.</p>
  <a class="btn">Read More</a>
  <div class="welcome-photo" role="img" aria-label="Photograph of a passport page with a visa stamp"></div>
</section>
<div class="section-rule" style="top:1005px"></div>

<section class="wrap services">
  <h2 class="section-title">Our Services</h2>
  <p class="section-lede">We Specialise in all sorts of Immigration Matters</p>
  <div class="service-grid">
    <div class="service">
      <div class="service-icon"><svg width="46" height="46" viewBox="0 0 46 46"><path d="M23 4c2 0 3 2 3 4v10l15 9v4l-15-4v9l5 4v3l-8-2-8 2v-3l5-4v-9L5 31v-4l15-9V8c0-2 1-4 3-4z" fill="var(--maroon)"/></svg></div>
      <h3>DEPENDANT VISAS</h3>
      <p>Help for spouses, partners and children joining family members who already live in the UK.</p>
      <a class="btn">Read More</a>
    </div>
    <div class="service">
      <div class="service-icon"><svg width="46" height="46" viewBox="0 0 46 46"><rect x="9" y="7" width="28" height="34" rx="2" fill="none" stroke="var(--maroon)" stroke-width="3"/><rect x="17" y="4" width="12" height="6" rx="1" fill="var(--maroon)"/><path d="M14 20l3 3 5-6M14 31l3 3 5-6" fill="none" stroke="var(--maroon)" stroke-width="2.4"/><line x1="25" y1="21" x2="33" y2="21" stroke="var(--maroon)" stroke-width="2.4"/><line x1="25" y1="32" x2="33" y2="32" stroke="var(--maroon)" stroke-width="2.4"/></svg></div>
      <h3>WORK PERMITS</h3>
      <p>Guidance for skilled workers, employers and sponsors through every stage of the permit process.</p>
      <a class="btn">Read More</a>
    </div>
    <div class="service">
      <div class="service-icon"><svg width="46" height="46" viewBox="0 0 46 46"><path d="M3 17l20-9 20 9-20 9z" fill="var(--maroon)"/><path d="M11 21v9c0 3 6 6 12 6s12-3 12-6v-9l-12 5z" fill="var(--maroon)"/><line x1="40" y1="18" x2="40" y2="32" stroke="var(--maroon)" stroke-width="2"/></svg></div>
      <h3>STUDENT VISAS</h3>
      <p>Support for students applying to study at colleges and universities anywhere in the UK.</p>
      <a class="btn">Read More</a>
    </div>
    <div class="service">
      <div class="service-icon"><svg width="46" height="46" viewBox="0 0 46 46"><rect x="6" y="9" width="34" height="31" rx="2" fill="none" stroke="var(--maroon)" stroke-width="3"/><rect x="6" y="9" width="34" height="8" fill="var(--maroon)"/><line x1="14" y1="5" x2="14" y2="12" stroke="var(--maroon)" stroke-width="3"/><line x1="32" y1="5" x2="32" y2="12" stroke="var(--maroon)" stroke-width="3"/><g fill="var(--maroon)"><rect x="11" y="21" width="5" height="4"/><rect x="20" y="21" width="5" height="4"/><rect x="29" y="21" width="5" height="4"/><rect x="11" y="29" width="5" height="4"/><rect x="20" y="29" width="5" height="4"/><rect x="29" y="29" width="5" height="4"/></g></svg></div>
      <h3>IMMIGRATION APPEALS</h3>
      <p>Strong representation at tribunal when an application has been refused or delayed unfairly.</p>
      <a class="btn">Read More</a>
    </div>
  </div>
</section>
<div class="section-rule" style="top:1460px"></div>

<section class="wrap team">
  <h2>Our Team Members</h2>
  <div class="pager"><i>‹</i><i>›</i></div>
  <div class="team-grid">
    <div class="member">
      <div class="member-photo" role="img" aria-label="Portrait photograph of attorney one in front of law books" style="background:linear-gradient(135deg,#8a5a3c,#d8c3a6)"></div>
      <h3>Attorney 1</h3>
      <p>Over ten years of practice in family and settlement cases across the UK.</p>
      <div class="member-social"><i class="c3"></i><i class="c2"></i><i class="c1"></i></div>
    </div>
    <div class="member">
      <div class="member-photo" role="img" aria-label="Portrait photograph of attorney two in a dark suit" style="background:linear-gradient(135deg,#5a1c22,#b68c78)"></div>
      <h3>Attorney 2</h3>
      <p>Leads our work permit team and advises employers on sponsor duties.</p>
      <div class="member-social"><i class="c3"></i><i class="c2"></i><i class="c1"></i></div>
    </div>
    <div class="member">
      <div class="member-photo" role="img" aria-label="Portrait photograph of attorney three seated at a desk" style="background:linear-gradient(135deg,#6b4a36,#caa889)"></div>
      <h3>Attorney 3</h3>
      <p>Handles student visas and appeals with care and clear communication.</p>
      <div class="member-social"><i class="c3"></i><i class="c2"></i><i class="c1"></i></div>
    </div>
    <div class="member">
      <div class="member-photo" role="img" aria-label="Portrait photograph of attorney four in front of law books" style="background:linear-gradient(135deg,#8a5a3c,#e0cbb0)"></div>
      <h3>Attorney 4</h3>
      <p>Specialist in detention and deportation matters at every tribunal level.</p>
      <div class="member-social"><i class="c3"></i><i class="c2"></i><i class="c1"></i></div>
    </div>
  </div>
</section>
<div class="section-rule" style="top:1915px"></div>

<section class="wrap news">
  <div class="news-list">
    <h2>News &amp; Publications</h2>
    <article class="news-item">
      <div class="news-photo" role="img" aria-label="Photograph of a consultation meeting in an office"></div>
      <div>
        <time>7 December 2015</time>
        <p>We handled a case where a Filipino national was in a relationship with an EU national. It was put to the officer that the Filipino was an overstayer. The first application was refused by another adviser and they came to see us in our London office.</p>
        <a class="more">Read More ›</a>
      </div>
    </article>
    <article class="news-item">
      <div class="news-photo" role="img" aria-label="Photograph of advisers reviewing documents together"></div>
      <div>
        <time>7 December 2015</time>
        <p>We handled a case where a Filipino national was in a relationship with an EU national. It was put to the officer that the Filipino was an overstayer. The first application was refused by another adviser and they came to see us in our London office.</p>
        <a class="more">Read More ›</a>
      </div>
    </article>
  </div>
  <aside class="sidebar">
    <h3>Immigration Law</h3>
    <ul>
      <li>Entry Clearance: Dependant Visas</li>
      <li>Immigration Appeals</li>
      <li>Settlement Applications (ILR)</li>
      <li>Domestic Workers Visa</li>
      <li>Student Visa</li>
      <li>Sponsorships</li>
      <li>Deportations</li>
      <li>Immigration Detention</li>
    </ul>
  </aside>
</section>

<footer class="site-footer">
  <div class="footer-cols">
    <div>
      <h4>Quick Links</h4>
      <ul class="footer-links"><li>Home</li><li>About Us</li><li>Join Us</li><li>Blog</li><li>Contact Us</li></ul>
    </div>
    <div class="newsletter">
      <h4>Sign up to Newsletter</h4>
      <p>Sign up to get the latest news and updates</p>
      <div class="field">Enter Email Address</div>
      <a class="btn">SUBMIT</a>
    </div>
    <div class="contact">
      <h4>Contact Us</h4>
      <ul>
        <li><b>Office:</b> Brackwell Counsel Partners, 14 Harrowden Road, London E9 4QP</li>
        <li><b>Mobile:</b> 0207 555 0142</li>
        <li><b>Fax:</b> 0207 555 0198</li>
        <li><b>Mail:</b> info@brackwellcounsel.co.uk</li>
      </ul>
    </div>
  </div>
</footer>
<div class="footer-bottom">
  <div class="copy">Copyright © 2015, Brackwell Counsel Partners. All Rights Reserved.</div>
  <div class="follow">FOLLOW US ON <i class="c2"></i><i class="c3"></i><i class="c4"></i><i class="c5"></i><i class="c6"></i></div>
</div>

</body>
</html>
```